Flyer for the Harvest of lanterns conference

Flyer design for an annual international conference called "MERIVAL 2017". This is a conference for young adults, so we hope to produce a design that is both professional and appealing to young people in general

We'd like the flyer to showcase the conference brand logo, and clearly highlight the key information to people who will read it.

Target Market(s)

Young people, young adults

Industry/Entity Type

Religious

Font styles to use
Sans Serif

Colors

Designer to choose colors to be used in the design.

Requirements
Must have
• - Should be only one page (Vertical or Horizontal).
• - the MERVAL logo and all the information found in the attached text file. This includes: Main topic: Your sons and daughters shall prophesy,
• Dates and time, location, contact information and everything that is in the attached text file.
Nice to have
• It would be nice to see samples where the white logo is used and another where the black one is used.
Should not have
• This is NOT a folded flyer, we will be sticking it on doors and public places. And we will be printing large simple to put on walls. So only one page with few words like an add (the words are in the attached file)

```html
<!DOCTYPE html>
<html lang="en">
<head>
<meta charset="utf-8">
<title>MERIVAL 2017 – Harvest of lanterns conference</title>
<link rel="stylesheet" href="https://fonts.googleapis.com/css2?family=Questrial&family=Encode+Sans+Semi+Condensed:wght@400;500&family=Open+Sans:wght@600;700&display=swap">
<style>
  :root {
    --ink: #111111;
    --gold: #e6a224;
    --red: #c8142c;
    --bright-red: #ec1c24;
    --navy: #1e2a6e;
    --venue-blue: rgba(20, 52, 140, 0.78);
    --panel: rgba(235, 238, 244, 0.82);
    --white: #ffffff;
  }
  * { margin: 0; padding: 0; box-sizing: border-box; }
  html, body { width: 848px; height: 1200px; overflow: hidden; }
  body { background: #ffffff; }
  .flyer {
    position: relative;
    width: 848px;
    height: 1200px;
    overflow: hidden;
    background:
      radial-gradient(ellipse 380px 300px at 650px 960px, rgba(40, 110, 230, 0.95), rgba(40, 110, 230, 0) 70%),
      radial-gradient(ellipse 300px 260px at 800px 1160px, rgba(10, 40, 150, 0.9), rgba(10, 40, 150, 0) 75%),
      radial-gradient(ellipse 420px 360px at 520px 520px, rgba(255, 255, 255, 1), rgba(255, 255, 255, 0) 70%),
      linear-gradient(120deg, #7e8ea8 0%, #c9d0dc 28%, #f4f6f9 55%, #dde6f4 72%, #5f8fe0 100%);
  }
  .backdrop { position: absolute; inset: 0; }
  .title {
    position: absolute; left: 56px; top: 66px;
    font-family: "Questrial", sans-serif;
    font-size: 106px; line-height: 1; letter-spacing: -1px;
    color: var(--ink);
    white-space: nowrap;
  }
  .title .year { color: var(--gold); font-family: "Open Sans", sans-serif; font-weight: 700; font-size: 100px; }
  .subtitle {
    position: absolute; left: 52px; top: 180px;
    font-family: "Questrial", sans-serif;
    font-size: 50px; line-height: 1; color: var(--red);
    white-space: nowrap;
  }
  .theme {
    position: absolute; left: 54px; top: 280px;
    font-family: "Encode Sans Semi Condensed", sans-serif;
    font-size: 54px; line-height: 78px; color: var(--bright-red);
  }
  .brand {
    position: absolute; left: 566px; top: 268px; width: 250px; text-align: center;
  }
  .brand-circle {
    width: 136px; height: 136px; margin: 0 auto;
    border-radius: 50%; border: 3px solid var(--gold);
  }
  .brand-name {
    margin-top: 10px;
    font-family: "Open Sans", sans-serif; font-weight: 700;
    font-size: 38px; letter-spacing: 4px; color: var(--ink);
  }
  .speakers {
    position: absolute; left: 0; top: 477px; width: 550px; height: 307px;
    background: var(--panel);
    padding: 24px 0 0 24px;
  }
  .speakers h2 {
    font-family: "Encode Sans Semi Condensed", sans-serif; font-weight: 400;
    font-size: 44px; line-height: 1; color: var(--gold); margin-bottom: 14px;
  }
  .speakers li {
    list-style: none;
    font-family: "Open Sans", sans-serif; font-weight: 600;
    font-size: 29px; line-height: 40px; color: var(--ink); white-space: nowrap;
  }
  .date-badge {
    position: absolute; left: 577px; top: 492px; width: 250px; height: 250px;
    border-radius: 50%; background: var(--bright-red); color: var(--white);
    font-family: "Encode Sans Semi Condensed", sans-serif; text-align: center;
    display: flex; flex-direction: column; justify-content: center;
  }
  .date-badge .month { font-size: 50px; line-height: 56px; }
  .date-badge .days, .date-badge .year { font-size: 38px; line-height: 44px; }
  .date-badge .time { font-size: 44px; line-height: 54px; }
  .venue {
    position: absolute; left: 568px; top: 780px; width: 280px; height: 250px;
    background: var(--venue-blue);
    padding: 10px 0 0 14px;
    font-family: "Encode Sans Semi Condensed", sans-serif;
    font-size: 28px; line-height: 38.5px; color: var(--white);
  }
  .room {
    position: absolute; left: 568px; top: 1064px; width: 280px; height: 68px;
    background: var(--gold);
    font-family: "Encode Sans Semi Condensed", sans-serif;
    font-size: 28px; line-height: 68px; padding-left: 14px; color: var(--ink);
  }
  .contacts {
    position: absolute; left: 30px; top: 866px; width: 450px;
    font-family: "Encode Sans Semi Condensed", sans-serif; color: var(--navy);
  }
  .contacts h2 {
    font-weight: 400; font-size: 46px; line-height: 1; color: var(--gold);
    text-align: center; margin-bottom: 30px; margin-left: 20px;
  }
  .contact-line {
    display: flex; align-items: center; gap: 12px;
    font-size: 30px; line-height: 1; height: 64px; white-space: nowrap;
  }
  .contact-line.phone { padding-left: 44px; }
  .contact-line.email { padding-left: 10px; }
  .contact-line.web { padding-left: 82px; }
  .contact-line svg { flex: none; }
</style>
</head>
<body>
<main class="flyer">
  <div class="backdrop" role="img" aria-label="Soft abstract background of silver-grey light fading into glowing blue swirls"></div>

  <h1 class="title">MERIVAL <span class="year">2017</span></h1>
  <p class="subtitle">harvest of lanterns conference</p>
  <p class="theme">Your Sons &amp; Daughters<br>Shall Prophesy</p>

  <div class="brand">
    <div class="brand-circle"></div>
    <div class="brand-name">MERVAL</div>
  </div>

  <section class="speakers">
    <h2>SPEAKERS</h2>
    <ul>
      <li>Prophet Lucien Marbeau</li>
      <li>Bishop Samuel Otieno</li>
      <li>Prophet Gabriel Nseko Mwamba</li>
      <li>Prophet Jonas Belaro</li>
      <li>Prophet Marc Tembo</li>
    </ul>
  </section>

  <div class="date-badge">
    <span class="month">Sept</span>
    <span class="days">1st, 2nd &amp; 3rd</span>
    <span class="year">2017</span>
    <span class="time">6:00PM</span>
  </div>

  <address class="venue" style="font-style:normal">
    Harborlight Garden<br>Inn<br>412 Elm Avenue<br>Fairhaven, ME<br>04210<br>United States
  </address>
  <div class="room">Birchwood Ballroom</div>

  <section class="contacts">
    <h2>CONTACTS</h2>
    <div class="contact-line phone">
      <svg width="32" height="32" viewBox="0 0 32 32" aria-hidden="true">
        <circle cx="16" cy="16" r="16" fill="#e6a224"/>
        <path d="M11 8c1 0 2 3 2.5 4 .4 1-1.5 2-1.2 2.8.8 2 2.5 3.8 4.6 4.7.8.3 1.8-1.6 2.8-1.2 1 .5 4 1.5 4 2.5 0 1.5-2 3.4-3.6 3.4C13.6 24.2 7.8 18.4 7.8 11.6 7.8 10 9.6 8 11 8z" fill="#fff"/>
      </svg>
      <span>+ 1 (207) 555 0148</span>
    </div>
    <div class="contact-line email">
      <svg width="34" height="34" viewBox="0 0 34 34" aria-hidden="true">
        <circle cx="17" cy="17" r="17" fill="#e6a224"/>
        <rect x="8.5" y="11" width="17" height="12" fill="none" stroke="#fff" stroke-width="2"/>
        <path d="M8.5 11l8.5 7 8.5-7M8.5 23l6-5.5M25.5 23l-6-5.5" fill="none" stroke="#fff" stroke-width="1.8"/>
      </svg>
      <span>hello@cedargrove.org</span>
    </div>
    <div class="contact-line web">
      <svg width="34" height="34" viewBox="0 0 34 34" aria-hidden="true">
        <g fill="none" stroke="#e6a224" stroke-width="2.4">
          <circle cx="17" cy="17" r="15"/>
          <ellipse cx="17" cy="17" rx="6.5" ry="15"/>
          <path d="M2 17h30M4.5 9h25M4.5 25h25M17 2v30"/>
        </g>
      </svg>
      <span>http://lanternhall.org</span>
    </div>
  </section>
</main>
</body>
</html>
```